Rosquillas de Maíz y Queso

Necesitamos el de una bolsa que sea parcialmente transparente, para este producto, nuestra empresa se llama TOVALSA (Comercial Tovalsa), estamos ubicados en Honduras. Este un producto típico de Honduras, Este producto es para consumo masivo y será vendido en supermercados.
Adjunto ejemplos de empaques de este producto ya existentes.
Updates

Es nuestra primera vez, y queremos revisar bien los diseños, adicionalmente unos nos llegaron ayer y queremos unos pequeños cambios para poder decidir. Gracias

Target Market(s)

Clientes en supermercados

Industry/Entity Type

Panaderia

Requirements
Must have
• La bolsa debe ser transparente con ventana para ver el producto
Nice to have
• Tiene que tener una ventana grande la bolsa o ser la mayor parte transparente para mostrar el producto

```html
<!DOCTYPE html>
<html lang="es">
<head>
<meta charset="utf-8">
<title>Rosquillas Queso – Empaque</title>
<link href="https://fonts.googleapis.com/css2?family=Bebas+Neue&family=Luckiest+Guy&family=Oswald:wght@700&display=swap" rel="stylesheet">
<style>
  :root {
    --page: #ffffff;
    --bag-red: #e8392a;
    --bag-orange: #f7892a;
    --title-red: #e02a1c;
    --gold: #f3c44a;
    --gold-light: #fbe79a;
    --ink: #2b1a12;
    --white: #ffffff;
    --window: #e4e4e4;
    --basket-light: #d08a45;
    --basket-dark: #8e5424;
  }
  html, body {
    margin: 0;
    padding: 0;
    width: 719px;
    height: 1200px;
    overflow: hidden;
    background: var(--page);
  }
  .canvas {
    position: relative;
    width: 719px;
    height: 1200px;
  }
  .bag-front {
    position: absolute;
    left: 60px;
    top: 50px;
    width: 600px;
    height: 848px;
    box-shadow: 0 6px 18px rgba(0,0,0,0.25);
  }
  .bag-front svg { display: block; }
  .brand-name {
    font-family: "Oswald", sans-serif;
    font-weight: 700;
    fill: var(--ink);
  }
  .product-title {
    font-family: "Oswald", sans-serif;
    font-weight: 700;
    fill: var(--white);
  }
  .claim {
    font-family: "Bebas Neue", sans-serif;
    fill: var(--ink);
  }
  .flavour {
    font-family: "Luckiest Guy", sans-serif;
    fill: var(--white);
  }
  .net-weight {
    font-family: "Oswald", sans-serif;
    font-weight: 700;
    fill: var(--white);
  }
  .window-legend {
    position: absolute;
    left: 0;
    top: 930px;
    width: 719px;
    text-align: center;
  }
  .window-legend__title {
    margin: 0 0 14px;
    font-family: "Bebas Neue", sans-serif;
    font-size: 30px;
    letter-spacing: 0.5px;
    color: #111;
  }
  .window-legend__swatch {
    display: inline-block;
    width: 280px;
    height: 190px;
    background: var(--window);
  }
</style>
</head>
<body>
<main class="canvas">
  <section class="bag-front">
    <svg width="600" height="848" viewBox="0 0 600 848" xmlns="http://www.w3.org/2000/svg">
      <defs>
        <radialGradient id="bagBackground" cx="50%" cy="45%" r="70%">
          <stop offset="0%" stop-color="#f9a233"/>
          <stop offset="60%" stop-color="#f26b2c"/>
          <stop offset="100%" stop-color="#e8392a"/>
        </radialGradient>
        <linearGradient id="goldStroke" x1="0" x2="1">
          <stop offset="0%" stop-color="#f6d36a"/>
          <stop offset="50%" stop-color="#fff3bd"/>
          <stop offset="100%" stop-color="#e8b43a"/>
        </linearGradient>
        <linearGradient id="basketTone" x1="0" y1="0" x2="0" y2="1">
          <stop offset="0%" stop-color="#d08a45"/>
          <stop offset="100%" stop-color="#8e5424"/>
        </linearGradient>
      </defs>

      <rect class="bag-background" width="600" height="848" fill="url(#bagBackground)"/>

      <g class="brand-mark">
        <circle cx="200" cy="105" r="9" fill="#2b1a12"/>
        <text class="brand-name" x="310" y="120" font-size="40" text-anchor="middle" letter-spacing="2">TOVALSA</text>
      </g>

      <g class="title-panel">
        <rect x="78" y="140" width="442" height="170" rx="30" fill="var(--title-red)" stroke="url(#goldStroke)" stroke-width="7"/>
        <text class="product-title" x="299" y="250" font-size="86" text-anchor="middle" letter-spacing="1" stroke="#3a120c" stroke-width="2" paint-order="stroke">ROSQUILLAS</text>
        <rect x="172" y="262" width="256" height="40" rx="20" fill="var(--gold-light)" stroke="var(--gold)" stroke-width="2"/>
        <text class="claim" x="300" y="292" font-size="30" text-anchor="middle">100% MAÍZ TOSTADO</text>
      </g>

      <g class="flavour-line">
        <line x1="90" y1="340" x2="210" y2="332" stroke="#ffffff" stroke-width="2"/>
        <line x1="390" y1="332" x2="510" y2="340" stroke="#ffffff" stroke-width="2"/>
        <text class="flavour" x="300" y="352" font-size="40" text-anchor="middle">QUESO</text>
      </g>

      <path class="product-window" d="M0,540 Q300,250 600,540 L600,760 L0,760 Z" fill="var(--window)" role="img" aria-label="Ventana transparente del empaque que muestra las rosquillas"/>
      <path class="window-rim" d="M0,540 Q300,250 600,540" fill="none" stroke="url(#goldStroke)" stroke-width="8"/>
      <path d="M30,470 Q300,290 570,470" fill="none" stroke="#ffffff" stroke-width="1.5" opacity="0.8"/>

      <path class="basket-band" d="M0,720 Q150,690 300,720 T600,705 L600,848 L0,848 Z" fill="url(#basketTone)" role="img" aria-label="Ilustración de canasta de mimbre"/>
      <text class="net-weight" x="505" y="785" font-size="30" text-anchor="middle" stroke="#5a2f10" stroke-width="2" paint-order="stroke">200g</text>
    </svg>
  </section>

  <aside class="window-legend">
    <p class="window-legend__title">ZONA TRANSPARENTE DEL EMPAQUE</p>
    <span class="window-legend__swatch" role="img" aria-label="Muestra de la zona transparente"></span>
  </aside>
</main>
</body>
</html>
```